Talent Agency Needs Identity!

We are Copper Harbor Artists Inc. - a full service entertainment services agency that focuses primarily on securing contracts for musicians and entertainers aboard luxury cruise ships, however we are not limited exclusively to that area, as we are expanding into the areas of film and television.

We are looking for the perfect website and logo from the right designer!

We already own the domain www.copperharborartists-demo.com

The homepage only needs to be designed for this contest, unless you really want to go that extra mile!

Would like full HTML and CSS3 if applicable.

Logo needs to be designed as well.

We have two primary colors that we want to use - Lime green and grey (or charcoal, slate, graphite etc.)

The pages should be mostly slate colored background, slightly peppered with green accents, tastefully incorporated.

The key target audience of the website will be artists and musicians seeking representation, but also entertainment executives sourcing our talent. We are focused on a refined, legitimate, clever image.

Some ideas for pages we have:
Home Page
About Us
Life At Sea
Apply Now
Contact Us
FAQ
Members Only Section

Some ideas for inspiration can be found at:
www.varnowtalent-demo.com
www.perkisound-demo.com
www.tidewrenhub-demo.com
www.quilbar-demo.com
www.delvoria-demo.com

The logo needs to be designed as well.

The logo should be simple, and communicate creativity, legitimacy, and current trends. Just a simple word logo. "Copper Harbor Artists", again with a refined, professional look and feel, with elements of creativity and cleverness incorporated.

We plan to expand into the areas of film and television - so this can be considered in the final design, which is why we have chosen the name Copper Harbor to begin with.

The term Copper Harbor in the context of the film industry means to formally approve a project's production finance, thereby allowing the project to move forward from the development phase to pre-production and principal photography.

Therefore, we want our image to be 'forward thinking and feeling'.

The website should be SEO optimized and include the following keywords:

cruise ship music gigs musicians jobs

Target Market(s)

Musicians, entertainment executives/buyers

Industry/Entity Type

Entertainment

Requirements
Must have
• Simple, easy to navigate design. An example of a website far too complicated:
www.rakuvance-demo.com

An example of a nice, clean website we like:
www.varnowtalent-demo.com
www.delvoria-demo.com
www.quilbar-demo.com
Nice to have
• A members only section where talent can log in to see their recruitment info.

A page for talent buyers.

A clean, enticing home page, leaving you curious to explore.

Should not have
• A busy, difficult to navigate interface.

Cheesy looking clip art.

```html
<!DOCTYPE html>
<html lang="en">
<head>
<meta charset="utf-8">
<title>Copper Harbor Artists – Cruise Ship Music Gigs &amp; Musicians Jobs</title>
<link rel="stylesheet" href="https://fonts.googleapis.com/css2?family=Cabin:wght@400;600&family=Lilita+One&family=Roboto+Condensed:wght@300;400;700&display=swap">
<style>
:root{
  --lime:#9cc41e;
  --lime-light:#b9dc3c;
  --lime-dark:#7fa612;
  --accent-text:#b3c92c;
  --charcoal:#1a1a1a;
  --slate:#2b2b2b;
  --panel:#e9e9e9;
  --caption:#101010;
  --ink:#3a3a3a;
  --muted:#8a8a8a;
  --orange:#f06a0c;
  --orange-light:#ff8f2e;
}
*{box-sizing:border-box;margin:0;padding:0}
html,body{width:1200px;height:1125px;overflow:hidden}
body{position:relative;background:var(--charcoal);font-family:Arial,Helvetica,sans-serif;color:#fff}
.backdrop{position:absolute;inset:0;
  background:
    radial-gradient(ellipse 260px 520px at 1150px 380px,rgba(170,190,90,.55),transparent 70%),
    radial-gradient(ellipse 240px 400px at 40px 520px,rgba(120,150,40,.55),transparent 70%),
    linear-gradient(180deg,#6f9a12 0%,#4a6a0c 12%,#2a3510 40%,#1b1d16 70%,#141414 100%);}
.page{position:absolute;left:141px;top:33px;width:919px}
.site-header{height:101px;position:relative;border:1px solid #a9d23a;
  background:linear-gradient(180deg,#b5dc3e 0%,#9ccb26 48%,#86bb12 50%,#8fc21b 100%)}
.brand{position:absolute;left:16px;top:18px;display:flex;align-items:center;gap:10px}
.brand-dot{width:52px;height:52px;border-radius:50%;background:#e8f5a8}
.brand-name{font-family:'Roboto Condensed',sans-serif;font-weight:700;font-size:25px;line-height:27px;color:#3b3b3b;text-transform:uppercase;letter-spacing:.5px}
.hotline{position:absolute;right:10px;top:11px;font-family:'Lilita One',sans-serif;font-size:25px;color:#f3e27a;
  -webkit-text-stroke:1px #4a3a10;letter-spacing:.5px}
.main-nav{position:absolute;right:10px;top:61px;display:flex;font-family:'Cabin',sans-serif;font-size:16px;color:#2f3a12}
.main-nav a{color:inherit;text-decoration:none}
.main-nav .sep{margin:0 10px}
.main-nav .current{border-bottom:1px solid #2f3a12;padding-bottom:1px}
.content{background:var(--panel);padding:15px 14px 15px;height:841px}
.slider{position:relative;width:890px;height:374px;
  background:linear-gradient(100deg,#2a1c3a 0%,#5a1a22 35%,#b02a36 60%,#3a1a20 80%,#5c5a10 100%)}
.slider-dots{position:absolute;right:12px;bottom:10px;display:flex;gap:6px}
.slider-dots span{width:10px;height:10px;border-radius:50%;background:#fff}
.slider-dots .active{background:var(--lime)}
.slide-caption{height:66px;background:var(--caption);font-family:'Roboto Condensed',sans-serif;font-weight:300;font-size:18px;color:#d8d8d8;padding:22px 15px}
.feature{margin-top:5px;height:368px;background:var(--slate);padding:9px 6px 0}
.categories{display:flex;gap:13px}
.card{width:209px;height:173px;background:#0c0c0c}
.card-photo{height:86px}
.card h3{font-family:'Roboto Condensed',sans-serif;font-weight:400;font-size:17px;color:var(--accent-text);text-align:center;margin-top:6px}
.card p{font-size:10.5px;line-height:16px;color:#6f6f6f;padding:0 7px;margin-top:1px}
.card .more{display:block;text-align:right;font-size:10px;color:var(--accent-text);padding-right:10px;margin-top:1px;text-decoration:none}
.careers{padding:12px 1px 0}
.careers h2{font-family:'Cabin',sans-serif;font-weight:400;font-size:17px;color:var(--accent-text)}
.careers .rule{border-top:2px dotted #5a5a5a;margin:6px 0 9px}
.careers p{font-size:11.5px;line-height:18px;color:#f0f0f0;padding-left:3px}
.careers .lead{width:870px;margin-bottom:16px}
.careers .pitch{width:690px}
.btn-apply{position:absolute;left:854px;top:893px;width:176px;height:56px;border-radius:4px;border:1px solid #ffb27a;
  background:linear-gradient(180deg,var(--orange-light),var(--orange));color:#fff;font-family:'Cabin',sans-serif;font-weight:600;font-size:24px;
  display:flex;align-items:center;justify-content:center;text-decoration:none}
.site-footer{position:absolute;left:141px;top:990px;width:919px;display:flex;justify-content:space-between;align-items:center}
.copyright{font-size:11.5px;color:#e6e6e6}
.social{display:flex;gap:10px}
.social span{width:22px;height:22px;border-radius:3px;background:#5a6b80}
</style>
</head>
<body>
<div class="backdrop" role="img" aria-label="Concert crowd and performer photograph in lime and dark tones"></div>
<div class="page">
  <header class="site-header">
    <div class="brand"><span class="brand-dot"></span><span class="brand-name">Copper Harbor<br>Artists</span></div>
    <div class="hotline">Call us @ 1-800-555-0147</div>
    <nav class="main-nav">
      <a class="current" href="#">Home</a><span class="sep">/</span>
      <a href="#">About us</a><span class="sep">/</span>
      <a href="#">Life at Sea</a><span class="sep">/</span>
      <a href="#">Apply Now</a><span class="sep">/</span>
      <a href="#">Contact us</a><span class="sep">/</span>
      <a href="#">Faq</a><span class="sep">/</span>
      <a href="#">Member Zone</a>
    </nav>
  </header>
  <main class="content">
    <section class="slider" role="img" aria-label="Band of musicians with guitars posing on a lit stage">
      <div class="slider-dots"><span></span><span class="active"></span><span></span></div>
    </section>
    <div class="slide-caption">Lorem Ipsum is simply dummy text of the</div>
    <section class="feature">
      <div class="categories">
        <article class="card"><div class="card-photo" role="img" aria-label="Theatre stage with purple curtain" style="background:linear-gradient(90deg,#6a2a14,#a04a1a 35%,#3a2a8a 55%,#8a3ad0)"></div><h3>CATEGORY NAME</h3><p>Lorem Ipsum is simply dummy text of the printing and typesetting industry. Lorem Ipsum has...</p><a class="more" href="#">Read more...</a></article>
        <article class="card"><div class="card-photo" role="img" aria-label="Singers at a microphone" style="background:linear-gradient(90deg,#140a08,#6a3020 40%,#c08060 70%,#201410)"></div><h3>CATEGORY NAME</h3><p>Lorem Ipsum is simply dummy text of the printing and typesetting industry. Lorem Ipsum has...</p><a class="more" href="#">Read more...</a></article>
        <article class="card"><div class="card-photo" role="img" aria-label="Guitarist performing on stage" style="background:linear-gradient(90deg,#1a2a20,#4a6a50 30%,#101812 55%,#5a7a60)"></div><h3>CATEGORY NAME</h3><p>Lorem Ipsum is simply dummy text of the printing and typesetting industry. Lorem Ipsum has...</p><a class="more" href="#">Read more...</a></article>
        <article class="card"><div class="card-photo" role="img" aria-label="Theatre stage with purple curtain" style="background:linear-gradient(90deg,#6a2a14,#a04a1a 35%,#3a2a8a 55%,#8a3ad0)"></div><h3>CATEGORY NAME</h3><p>Lorem Ipsum is simply dummy text of the printing and typesetting industry. Lorem Ipsum has...</p><a class="more" href="#">Read more...</a></article>
      </div>
      <div class="careers">
        <h2>Exciting Careers At Sea</h2>
        <div class="rule"></div>
        <p class="lead">We offer a range of representation services--all designed to help you reach your potential. We place musicians on luxury cruise ships sailing on exotic itineraries all over the world, as well as in world class venue's such as Las Vegas hotels, casino's, and theaters. We have partnered with the world's leading cruise lines and have direct access to the jobs you want.</p>
        <p class="pitch">Whatever your situation - if you're thinking about your first gig on a cruise ship, or perhaps making a move to a new cruise line or position, we are on the front lines and work to get you what you want at a rate you deserve.</p>
      </div>
    </section>
  </main>
</div>
<a class="btn-apply" href="#">Apply Now</a>
<footer class="site-footer">
  <p class="copyright">Copyright © 2012. COPPERHARBORARTISTS-DEMO.COM. All rights reserved.</p>
  <div class="social" aria-label="Social links"><span></span><span></span><span></span><span></span><span></span></div>
</footer>
</body>
</html>
```